Simple infographic for paper attributes

Hello, we are a company that sells paper. Any kind of paper, envelopes, letter paper, handicraft paper etc.

We need a graphic / infographic which indicates to our customers that our paper / envelopes etc. are both printable with printers and writable with any pens.

Font styles to use
Serif
Sans Serif

Requirements
Must have
• - The format would be 3000x3000 pixels.
- The style would be simple and simple
Nice to have
• - The two terms "printable" and "writable" may be used

```html
<!DOCTYPE html>
<html lang="en">
<head>
<meta charset="utf-8">
<title>Writable and Printable Paper</title>
<link href="https://fonts.googleapis.com/css2?family=Quicksand:wght@300;400&display=swap" rel="stylesheet">
<style>
  :root {
    --page: #ffffff;
    --sky: #72a3d3;
    --line: #ffffff;
    --ink-blue: #1a6fc4;
  }
  html, body {
    margin: 0;
    padding: 0;
    width: 1200px;
    height: 848px;
    overflow: hidden;
    background: var(--page);
  }
  .canvas {
    position: relative;
    width: 1200px;
    height: 848px;
    background: var(--page);
  }
  .infographic {
    position: absolute;
    left: 0;
    top: 0;
    width: 1200px;
    height: 848px;
  }
  .attribute-label {
    position: absolute;
    width: 202px;
    text-align: center;
    font-family: "Quicksand", sans-serif;
    font-weight: 300;
    font-size: 29px;
    color: var(--line);
    letter-spacing: 0.2px;
    top: 478px;
    margin: 0;
    line-height: 1;
  }
  .attribute-label--writable { left: 145px; }
  .attribute-label--printable { left: 851px; }
</style>
</head>
<body>
<main class="canvas">
  <svg class="infographic" viewBox="0 0 843 596" preserveAspectRatio="none" aria-hidden="true">
    <rect class="backdrop" x="0" y="41" width="843" height="513" fill="var(--sky)"/>

    <g class="connectors" stroke="var(--line)" stroke-width="1" fill="none">
      <line x1="244" y1="310" x2="265" y2="310"/>
      <line x1="578" y1="310" x2="599" y2="310"/>
    </g>

    <g class="rings" stroke="var(--line)" stroke-width="1" fill="none">
      <circle cx="421" cy="297" r="157"/>
      <circle cx="173" cy="315" r="71"/>
      <circle cx="669" cy="315" r="71"/>
    </g>

    <g class="paper-icon">
      <polygon points="370,195 490,195 490,385 340,385 340,228" fill="var(--line)"/>
      <polygon points="383,208 502,208 502,396 352,396 352,240" fill="none" stroke="var(--ink-blue)" stroke-width="1.4"/>
      <polyline points="352,240 383,240 383,208" fill="none" stroke="var(--ink-blue)" stroke-width="1.4"/>
      <g stroke="var(--ink-blue)" stroke-width="1.4">
        <line x1="385" y1="277" x2="468" y2="277"/>
        <line x1="385" y1="308" x2="468" y2="308"/>
        <line x1="385" y1="338" x2="468" y2="338"/>
      </g>
    </g>

    <g class="pen-icon" stroke="var(--line)" stroke-width="1" fill="none" stroke-linejoin="round">
      <polygon points="140,320 146,306 190,264 196,270 152,313"/>
      <line x1="146" y1="306" x2="152" y2="313"/>
      <line x1="190" y1="264" x2="193" y2="261"/>
      <polyline points="193,261 199,267 196,270"/>
      <line x1="163" y1="284" x2="180" y2="268"/>
      <line x1="140" y1="325" x2="207" y2="325"/>
    </g>

    <g class="printer-icon" stroke="var(--line)" stroke-width="1" fill="none" stroke-linejoin="round">
      <rect x="650" y="270" width="40" height="10"/>
      <rect x="634" y="280" width="72" height="35" rx="4"/>
      <polyline points="650,305 650,332 684,332 690,326 690,305"/>
      <polyline points="684,332 684,326 690,326"/>
      <circle cx="696" cy="289" r="1.3"/>
      <circle cx="696" cy="294" r="1.3"/>
    </g>
  </svg>

  <p class="attribute-label attribute-label--writable">Writable</p>
  <p class="attribute-label attribute-label--printable">Printable</p>
</main>
</body>
</html>
```